A guide to healing depression needs a great cover

An experienced therapist and former patient have put together a great guide to help people living with depression and their loved ones.
With the extraordinary combination of real case studies, checklists, clearly formulated medical content, helpful and detailed steps and practical exercises, everyone can learn how to put their own life back on the right track. We put an end to the constant worries, rebuild your self-esteem and start with positive thoughts into a happy future.
We imagine the sufferer coming out of the darkness and walking into the sunrise (or something like that). A very bright cover, which symbolizes light, would also be possible. Attached you will find an image that appealed to us, but which seems too cheap.

Target Market(s)

Depressed people and their families

Font styles to use
Serif

Requirements
Must have
• go from darkness into light
Nice to have
• For the title, it would be great if the word depression were highlighted
Should not have
• don't look cheap

```html
<!DOCTYPE html>
<html lang="de">
<head>
<meta charset="utf-8">
<title>Hallo Schwermut – jetzt ist Schluss!</title>
<link href="https://fonts.googleapis.com/css2?family=Cinzel:wght@400;500&family=Open+Sans:ital,wght@0,400;1,700&family=Arimo&display=swap" rel="stylesheet">
<style>
  :root {
    --sky-top: #c90a06;
    --sky-mid: #f05a10;
    --sky-glow: #ffd21a;
    --sun-core: #fff36a;
    --night: #030303;
    --orange: #e8520c;
    --amber: #f29d0a;
    --gold: #f9c91a;
    --white: #ffffff;
    --tool-orange: #f3a20c;
  }
  * { margin: 0; padding: 0; box-sizing: border-box; }
  html, body {
    width: 840px; height: 1200px; overflow: hidden;
    background: var(--night);
  }
  .cover {
    position: relative; width: 840px; height: 1200px;
    background: var(--night); overflow: hidden;
  }
  .sunrise-art {
    position: absolute; left: 0; top: 0; width: 840px; height: 660px;
    background:
      radial-gradient(ellipse 420px 380px at 50% 92%, var(--sun-core) 0%, var(--sky-glow) 22%, #f9a312 45%, transparent 80%),
      linear-gradient(to bottom, var(--sky-top) 0%, #e2300b 30%, var(--sky-mid) 60%, #f7a015 100%);
  }
  .horizon {
    position: absolute; left: 0; top: 630px; width: 840px; height: 40px;
    background: linear-gradient(to bottom, rgba(3,3,3,0) 0%, var(--night) 70%);
  }
  .authors {
    position: absolute; left: 0; right: 0; top: 70px;
    text-align: center; color: var(--white);
    font-family: "Arimo", Arial, sans-serif; font-size: 36px;
  }
  .title {
    position: absolute; left: 0; top: 668px; width: 840px;
    text-align: center; font-family: "Cinzel", serif; font-weight: 400;
  }
  .title-lead {
    display: block; font-size: 44px; line-height: 52px;
    color: var(--white); letter-spacing: 6px;
  }
  .title-word {
    display: block; font-size: 92px; line-height: 108px;
    color: var(--gold);
  }
  .title-tagline {
    display: block; margin-top: 6px; font-size: 46px; line-height: 56px;
    color: var(--white); letter-spacing: 10px;
  }
  .series {
    position: absolute; left: 0; right: 0; top: 956px;
    text-align: center; color: var(--tool-orange);
    font-family: "Open Sans", sans-serif; font-weight: 700; font-style: italic;
    font-size: 32px; letter-spacing: 3px;
  }
  .blurb {
    position: absolute; left: 0; right: 0; top: 1012px;
    text-align: center; color: var(--white);
    font-family: "Open Sans", sans-serif; font-size: 23px; line-height: 27px;
  }
</style>
</head>
<body>
  <main class="cover">
    <div class="sunrise-art" role="img" aria-label="Sonnenaufgang mit Strahlen hinter einer Wiese, Silhouetten eines Erwachsenen und eines Kindes mit ausgebreiteten Armen"></div>
    <div class="horizon"></div>

    <p class="authors">Dipl.-Psych. Jonas Albrecht &amp; Matthias Lerner</p>

    <h1 class="title">
      <span class="title-lead">HALLO</span>
      <span class="title-word">SCHWERMUT –</span>
      <span class="title-tagline">JETZT IST SCHLUSS!</span>
    </h1>

    <p class="series">ALLTAGSHILFEN AUS DER PRAXIS</p>
    <p class="blurb">
      Mit erprobten Übungen &amp; Fallbeispielen<br>
      aus langjähriger Praxis trübe Gedanken und<br>
      Schwermut hinter sich lassen – für Betroffene &amp; Familie
    </p>
  </main>
</body>
</html>
```